Wine label refresh

We are wanting to modify our Corran Estate label to include a picture on it.
I have attached the pictures below which we would like on the label. They are of the Corran Estate vineyard. I have also attached an example of another label with a picture on it that we like the style of.
Industry/Entity Type
Vineyard
Requirements
Must have
- The Corran Estate text must stay the same but can be moved down. It still needs to be the same size though.
Marlborough Sauvignon Blanc should remain in the same font and roughly the same size.
Wine of New Zealand also must stay but could potentially be moved.
Nice to have
- It would be nice if we could keep the KL logo on the front label but feel free to experiment with where this goes.

```html
<!DOCTYPE html>
<html lang="en">
<head>
<meta charset="utf-8">
<title>Corran Estate – Marlborough Sauvignon Blanc 2012 label</title>
<link rel="stylesheet" href="https://fonts.googleapis.com/css2?family=Cormorant+SC:wght@500&family=Pinyon+Script&family=Lato:wght@300&display=swap">
<style>
  :root {
    --amber: #d78b0b;
    --cut-guide: #2fd6e6;
    --ink: #111111;
    --wine-red: #c81e2a;
    --paper: #ffffff;
    --sepia-dark: #5a5335;
    --sepia-mid: #a9a47c;
    --sepia-light: #e6e4cc;
  }
  html, body {
    margin: 0;
    padding: 0;
    overflow: hidden;
    background: var(--paper);
  }
  .canvas {
    position: relative;
    width: 1200px;
    height: 1001px;
    background: var(--paper);
    overflow: hidden;
  }
  .canvas > * { position: absolute; }
  .label-frames { left: 0; top: 0; }

  .vineyard-photo {
    left: 117px;
    top: 171px;
    width: 970px;
    height: 335px;
    background: linear-gradient(180deg,
      var(--sepia-dark) 0%,
      var(--sepia-mid) 45%,
      var(--sepia-light) 78%,
      var(--paper) 100%);
  }

  .estate-monogram {
    left: 0;
    width: 1200px;
    top: 360px;
    text-align: center;
    font-family: "Cormorant SC", serif;
    font-weight: 500;
    font-size: 110px;
    line-height: 1;
    color: var(--ink);
  }

  .estate-name {
    left: 0;
    width: 1200px;
    top: 515px;
    text-align: center;
    font-family: "Cormorant SC", serif;
    font-weight: 500;
    font-size: 96px;
    line-height: 1;
    letter-spacing: 6px;
    color: var(--ink);
  }

  .wine-variety, .vintage {
    left: 0;
    width: 1200px;
    text-align: center;
    font-family: "Pinyon Script", cursive;
    color: var(--wine-red);
    line-height: 1;
  }
  .wine-variety { top: 628px; font-size: 54px; }
  .vintage { top: 696px; font-size: 50px; }

  .legal-band {
    left: 117px;
    top: 762px;
    width: 970px;
    height: 76px;
    display: flex;
    align-items: center;
    justify-content: space-between;
    padding: 0 14px;
    box-sizing: border-box;
    font-family: "Lato", sans-serif;
    font-weight: 300;
    font-size: 34px;
    color: var(--paper);
  }
</style>
</head>
<body>
<main class="canvas">
  <svg class="label-frames" width="1200" height="1001" viewBox="0 0 1200 1001" aria-hidden="true">
    <rect x="1" y="1" width="1198" height="999" fill="none" stroke="var(--ink)" stroke-width="2"/>
    <rect x="23" y="71" width="1158" height="862" rx="6" fill="none" stroke="var(--cut-guide)" stroke-width="2"/>
    <rect x="47" y="99" width="1110" height="804" fill="none" stroke="var(--amber)" stroke-width="2"/>
    <rect x="70" y="126" width="1063" height="754" fill="var(--amber)"/>
    <rect x="103" y="158" width="998" height="690" fill="var(--paper)"/>
    <rect x="115" y="169" width="974" height="671" fill="none" stroke="var(--amber)" stroke-width="2"/>
    <rect x="116" y="761" width="972" height="78" fill="var(--amber)"/>
  </svg>

  <div class="vineyard-photo" role="img" aria-label="Sepia photograph of the estate vineyard: rows of vines leading to a homestead among palm trees, with hills behind, fading to white at the bottom"></div>

  <div class="estate-monogram">KL</div>
  <h1 class="estate-name" style="margin:0">Corran Estate</h1>
  <div class="wine-variety">Marlborough Sauvignon Blanc</div>
  <div class="vintage">2012</div>

  <div class="legal-band">
    <span class="volume">750ml</span>
    <span class="origin">NEW ZEALAND WINE</span>
    <span class="alcohol">13% alc/vol</span>
  </div>
</main>
</body>
</html>
```